Business software developers new website

We need to redesign our website. Our current website is http://www.plumvista.net/index.html, which is outdated and needs a new look. We moved out from web design and have concentrated more on the back end of the systems, for example, system support and security and cloud-based applications. Our major clients include both private and government sectors. We would like to see some designs that are all in one page, simple and clean. Prefer illustrator or obstructed images instead of real-life photos. Must look futuristic yet friendly. Attached the new logo for your references and good luck.

Target Market(s)

Medium to big company for their IT or data management. Either improve or upgrade their current system.

Industry/Entity Type

Business Software

Number of Pages Required

1 page

Colors

Designer to choose colors to be used in the design.

Requirements
Must have
• Simple and clean. Individual assets must be provided in the correct size and format(png or jpeg). Prefer Goggle fonts. Even though the logo color is red, grey and black, still prefer some modern colors that go well with red. When design, must consider the possibility to convert it into responsive.
Nice to have
• White background
Should not have
• real life photos, no slider

```html
<!DOCTYPE html>
<html lang="en">
<head>
<meta charset="utf-8">
<title>plumvista.net</title>
<link href="https://fonts.googleapis.com/css2?family=Raleway:wght@400;500;600;700&display=swap" rel="stylesheet">
<style>
:root{
  --steel:#6a8fa8;
  --ink:#141414;
  --white:#ffffff;
  --line:#d9dde0;
  --sky:#5bb8f5;
  --coral:#e74c3c;
  --navy:#2c3e50;
  --muted:#9a9a9a;
}
*{margin:0;padding:0;box-sizing:border-box}
html,body{width:1200px;height:3386px;overflow:hidden}
body{position:relative;background:var(--white);font-family:'Raleway',sans-serif;color:var(--ink)}
.abs{position:absolute}
.topbar{left:0;top:0;width:1200px;height:6px;background:var(--steel)}
.header{left:0;top:6px;width:1200px;height:87px;background:var(--white);border-bottom:2px solid #e2e6e9}
.logo{left:234px;top:26px;font-size:38px;font-weight:500;letter-spacing:-0.5px;color:var(--ink);display:flex;align-items:center;gap:8px}
.logo-dot{width:14px;height:14px;border-radius:50%;background:var(--coral)}
.nav a{position:absolute;top:40px;transform:translateX(-50%);font-size:12px;font-weight:700;color:var(--ink);text-decoration:none}
.nav-marker{left:654px;top:6px;width:0;height:0;border-left:5px solid transparent;border-right:5px solid transparent;border-top:7px solid var(--steel)}

.hero{left:0;top:93px;width:1200px;height:531px;background:var(--steel)}
.hero-content{left:234px;top:200px;width:390px;display:flex;flex-direction:column}
.hero-title{font-size:30px;font-weight:700;line-height:36px;white-space:nowrap}
.hero-text{margin-top:10px;width:375px;font-size:14.5px;line-height:18px;font-weight:500}
.hero-content .btn{margin-top:30px}
.hero-art{left:625px;top:255px;width:575px;height:238px;background:linear-gradient(110deg,#9fb8c8 0%,#e9eef1 40%,#33475a 70%,#e8632c 100%);opacity:.9}

.btn{display:flex;align-items:center;justify-content:center;width:156px;height:37px;font-size:14px;font-weight:700;text-decoration:none}
.btn-light{background:var(--white);color:var(--ink)}
.btn-steel{background:var(--steel);color:var(--white)}
.section-title{left:0;width:1200px;text-align:center;font-size:31px;font-weight:700}

.about-text{left:234px;top:800px;width:380px;font-size:14.5px;line-height:18px;font-weight:500}
.about-grid{left:653px;top:802px;width:313px;height:313px;display:grid;grid-template-columns:1fr 1fr}
.about-grid div{display:flex;align-items:flex-end;justify-content:center;font-size:8px;padding:4px;color:var(--white)}
.about-grid .tile-cloud{background:#f1f5f8;color:var(--ink)}
.about-grid .tile-apps{background:var(--sky)}
.about-grid .tile-security{background:var(--coral);align-items:flex-start}
.about-grid .tile-support{background:var(--navy);align-items:flex-start}

.service{width:188px;height:186px;background:var(--steel);display:flex;align-items:center;justify-content:center}
.service-label{width:188px;text-align:center;font-size:19px;font-weight:700}

.clients-intro{left:234px;top:1785px;width:735px;font-size:19px;line-height:22.5px;font-weight:500}
.client{width:200px}
.client h3{font-size:23px;font-weight:700;line-height:26px}
.client p{font-size:14.5px;line-height:18px;font-weight:500}
.grid-v{width:2px;height:251px;top:1899px;background:var(--navy)}
.grid-h{left:234px;top:2024px;width:732px;height:2px;background:var(--navy)}

.faq{left:234px;top:2320px;width:732px}
.faq-row{display:flex;justify-content:space-between;align-items:center;height:31px;border-bottom:1px solid var(--line);font-size:15px;font-weight:600}
.caret{width:0;height:0;border-left:5px solid transparent;border-right:5px solid transparent;border-top:5px solid var(--ink);margin-right:4px}

.field{font-size:14px;font-weight:700;border-bottom:2px solid var(--steel);padding-bottom:6px}
.field .req{color:var(--muted);font-weight:400;font-size:10px;vertical-align:top;margin-left:2px}
.contact-icon{left:748px;width:30px;height:30px}
.contact-rule{left:783px;width:2px;height:44px;background:var(--ink)}
.contact-item{left:795px}
.contact-item b{display:block;font-size:14px;color:var(--steel);font-weight:700}
.contact-item span{display:block;font-size:19px;font-weight:500}

.subscribe{left:0;top:3010px;width:1200px;height:63px;background:var(--steel)}
.sub-input{left:360px;top:3035px;width:312px;font-size:18px;color:var(--white);border-bottom:1px solid #dbe4ea;padding-bottom:4px;font-weight:500}
.sub-btn{left:685px;top:3023px;width:156px;height:37px;border:2px solid var(--white);color:var(--white);font-size:18px;font-weight:700;display:flex;align-items:center;justify-content:center}

.footer{left:0;top:3198px;width:1200px;height:188px;background:var(--steel)}
.foot-nav{left:0;top:3259px;width:1200px;display:flex;justify-content:center;align-items:center;color:var(--white);font-size:15px;font-weight:700}
.foot-nav a{color:var(--white);text-decoration:none}
.foot-nav i{font-style:normal;margin:0 38px}
.social{left:560px;top:3304px;display:flex;gap:5px}
.social span{width:16px;height:16px;background:var(--white);border-radius:2px}
.copyright{left:0;top:3372px;width:1200px;text-align:center;font-size:7px;color:var(--white)}
.to-top{left:934px;top:3355px;width:32px;height:31px;background:var(--white);display:flex;align-items:center;justify-content:center}
</style>
</head>
<body>

<div class="abs topbar"></div>
<header class="abs header"></header>
<div class="abs nav-marker"></div>
<div class="abs logo">plumvista<span class="logo-dot"></span>net</div>
<nav class="nav">
  <a href="#home" style="left:657px">HOME</a>
  <a href="#about" style="left:720px">ABOUT</a>
  <a href="#services" style="left:793px">SERVICES</a>
  <a href="#clients" style="left:866px">CLIENT</a>
  <a href="#contact" style="left:940px">CONTACT</a>
</nav>

<section class="abs hero" id="home"></section>
<div class="abs hero-art" role="img" aria-label="Flat illustration of a globe, envelopes, reports, a calendar and a laptop dashboard beside a row of server binders"></div>
<div class="abs hero-content">
  <h1 class="hero-title">Lorem Ipsum is simply<br>dummy text of the printing<br>and typesetting industry</h1>
  <p class="hero-text">We have provided system support, security and cloud-based application solutions for a wide variety of industries. We are known for the quality of our work, affordable rates and our individual approach to each customer. Our company offers a wide variety of professional back-end solutions and all this at very competitive prices!</p>
  <a class="btn btn-light" href="#about">LEARN MORE</a>
</div>

<h2 class="abs section-title" id="about" style="top:741px">ABOUT US</h2>
<div class="abs about-text">
  <p>Plumvista.net is an Australian based Software and Systems Company that provides individual technology solutions and professional software for clients worldwide.<br>Our work is based on quality sales, customer and technical support services.</p>
  <p style="margin-top:18px">Being oriented towards innovative productivity in our work, we come up with essential tools for online business enhancing. Our programming specialists focus on delivering solutions for small start-ups as well as large organizations and companies. The team of purposeful and experienced professionals works hard to extract maximum performance from modern information technologies.<br>Providing the best quality of service and excellence of support we established a global presence in the software market. Our clients come from all over the world.</p>
</div>
<div class="abs about-grid">
  <div class="tile-cloud" role="img" aria-label="Isometric cloud computing illustration">Cloud Computing</div>
  <div class="tile-apps" role="img" aria-label="Isometric cloud application illustration">Cloud Applications</div>
  <div class="tile-security" role="img" aria-label="Isometric system security illustration">System Security</div>
  <div class="tile-support" role="img" aria-label="Isometric system support illustration">System Support</div>
</div>
<a class="abs btn btn-steel" href="#services" style="left:234px;top:1155px">LEARN MORE</a>

<h2 class="abs section-title" id="services" style="top:1308px">OUR SERVICES</h2>
<div class="abs service" style="left:234px;top:1370px">
  <svg width="110" height="110" viewBox="0 0 110 110" fill="none" stroke="#fff" stroke-width="7" stroke-linejoin="round">
    <circle cx="55" cy="55" r="18"/>
    <path d="M55 14v14M55 82v14M14 55h14M82 55h14M26 26l10 10M74 74l10 10M26 84l10-10M74 36l10-10"/>
  </svg>
</div>
<div class="abs service" style="left:506px;top:1370px">
  <svg width="110" height="120" viewBox="0 0 110 120" fill="none" stroke="#fff" stroke-width="7" stroke-linejoin="round">
    <path d="M55 10L16 24v32c0 26 17 44 39 54 22-10 39-28 39-54V24z"/>
    <path d="M36 60l13 13 26-28"/>
  </svg>
</div>
<div class="abs service" style="left:778px;top:1370px">
  <svg width="130" height="100" viewBox="0 0 130 100" fill="none" stroke="#fff" stroke-width="7" stroke-linejoin="round">
    <path d="M36 80h64a20 20 0 0 0 2-40 30 30 0 0 0-58-6 23 23 0 0 0-8 46z"/>
  </svg>
</div>
<div class="abs service-label" style="left:234px;top:1582px">System Support</div>
<div class="abs service-label" style="left:506px;top:1582px">Security</div>
<div class="abs service-label" style="left:778px;top:1582px">Cloud Applications</div>

<h2 class="abs section-title" id="clients" style="top:1722px;font-weight:600">Our Clients</h2>
<p class="abs clients-intro">Lorem Ipsum is simply dummy text of the printing and typesetting industry. Lorem Ipsum has been the industry's standard dummy text ever since the 1500s, when an unknown printer took a galley of type and scrambled it to make a type specimen book.</p>
<div class="abs grid-v" style="left:453px"></div>
<div class="abs grid-v" style="left:745px"></div>
<div class="abs grid-h"></div>
<div class="abs client" style="left:234px;top:1922px"><h3>John Doe</h3><p>Lorem Ipsum is simply dummy text of the printing and typesetting industry.</p></div>
<div class="abs client" style="left:506px;top:1922px"><h3>John Doe</h3><p>Lorem Ipsum is simply dummy text of the printing and typesetting industry.</p></div>
<div class="abs client" style="left:778px;top:1922px"><h3>John Doe</h3><p>Lorem Ipsum is simply dummy text of the printing and typesetting industry.</p></div>
<div class="abs client" style="left:234px;top:2049px"><h3>John Doe</h3><p>Lorem Ipsum is simply dummy text of the printing and typesetting industry.</p></div>
<div class="abs client" style="left:506px;top:2049px"><h3>John Doe</h3><p>Lorem Ipsum is simply dummy text of the printing and typesetting industry.</p></div>
<div class="abs client" style="left:778px;top:2049px"><h3>John Doe</h3><p>Lorem Ipsum is simply dummy text of the printing and typesetting industry.</p></div>

<h2 class="abs section-title" style="top:2269px;font-weight:600">Frequently Asked Questions</h2>
<div class="abs faq">
  <div class="faq-row">Lorem Ipsum is<span class="caret"></span></div>
  <div class="faq-row">Lorem Ipsum is simply<span class="caret"></span></div>
  <div class="faq-row">Lorem Ipsum is simply dummy text<span class="caret"></span></div>
  <div class="faq-row">Lorem Ipsum is simply dummy text of the printing and typesetting industry<span class="caret"></span></div>
  <div class="faq-row">Lorem Ipsum is simply dummy text of the printing and typesetting industry<span class="caret"></span></div>
</div>

<h2 class="abs section-title" id="contact" style="top:2592px;font-weight:600">Get In Touch!</h2>
<div class="abs field" style="left:234px;top:2668px;width:188px">Enter &nbsp;Name<span class="req">*</span></div>
<div class="abs field" style="left:441px;top:2668px;width:189px">Enter &nbsp;Email<span class="req">*</span></div>
<div class="abs field" style="left:234px;top:2714px;width:396px">Enter &nbsp;Subject<span class="req">*</span></div>
<div class="abs field" style="left:234px;top:2763px;width:396px;height:48px">Message<span class="req">*</span></div>
<a class="abs btn btn-steel" href="#contact" style="left:234px;top:2848px">SUBMIT</a>

<svg class="abs contact-icon" style="top:2660px" viewBox="0 0 30 30"><path d="M15 2a9 9 0 0 0-9 9c0 7 9 17 9 17s9-10 9-17a9 9 0 0 0-9-9z" fill="var(--steel)"/><circle cx="15" cy="11" r="3.5" fill="#fff"/></svg>
<div class="abs contact-rule" style="top:2656px"></div>
<div class="abs contact-item" style="top:2651px"><b>Address</b><span>48 Larkfield Row NE</span></div>
<svg class="abs contact-icon" style="top:2728px" viewBox="0 0 30 30"><path d="M6 3l6 1 2 7-4 3c2 4 4 6 8 8l3-4 7 2 1 6c-2 2-4 3-7 2C13 26 5 18 3 10 2 7 4 4 6 3z" fill="var(--steel)"/></svg>
<div class="abs contact-rule" style="top:2724px"></div>
<div class="abs contact-item" style="top:2719px"><b>Phone</b><span>555-014-2738</span></div>
<svg class="abs contact-icon" style="top:2795px" viewBox="0 0 30 30" fill="none" stroke="var(--steel)" stroke-width="2"><rect x="2" y="6" width="26" height="18"/><path d="M2 6l13 11L28 6"/></svg>
<div class="abs contact-rule" style="top:2790px"></div>
<div class="abs contact-item" style="top:2785px"><b>Email</b><span>hello@plumvista.net</span></div>

<section class="abs subscribe"></section>
<div class="abs sub-input">Enter Your Email</div>
<div class="abs sub-btn">Subscribe</div>

<footer class="abs footer"></footer>
<nav class="abs foot-nav">
  <a href="#home">HOME</a><i>|</i><a href="#about">ABOUT</a><i>|</i><a href="#services">SERVICES</a><i>|</i><a href="#clients">CLIENT</a><i>|</i><a href="#contact">CONTACT</a>
</nav>
<div class="abs social" aria-label="Social links">
  <span></span><span></span><span></span><span></span>
</div>
<div class="abs copyright">Copyright 2021 | Plumvista.net</div>
<a class="abs to-top" href="#home" aria-label="Back to top">
  <svg width="18" height="18" viewBox="0 0 18 18"><path d="M9 2L2 9h4v7h6V9h4z" fill="var(--steel)"/></svg>
</a>

</body>
</html>
```